Redesign two existing website pages and one new landing page for dental office

I need to redesign two webpages on my dental website, the Home page (http://brelvoortdental.com) and the Dental Implant Services page (http://www.brelvoortdental.com/dental-implant-services) and also create a landing page for the Dental Implant Services page.

Please use the same color scheme, slogans and subtitles for the redesign pages and create a reserved video spot on each page. The video spots should not be too big but not too small either and positioned in a central key location on each of the pages. The final redesigned pages should communicate leadership, confidence and trust.

The new landing page for the Dental implant Services page must not have any hyperlinks on the page and must entice the viewer to give name and email before downloading a "Free" eBook called "Is a Fresh Smile Worth Waiting For?" Any added photo images to this new page must be smiling.
Updates

Project Deadline Extended Reason: I got feedback that my project was not long enough so I'm extending it by 5 days. Added Thursday, April 16, 2015

Target Market(s)

People who are middle-age to seniors.

Industry/Entity Type

Dental

Coding

Coded - Design and coding required

Number of Pages Required

3 page

Requirements
Must have
• Compatible with existing website colors and theme.

```html
<!DOCTYPE html>
<html lang="en">
<head>
<meta charset="utf-8">
<title>Brelvoort Dental Care</title>
<link href="https://fonts.googleapis.com/css2?family=Oxygen:wght@400;700&display=swap" rel="stylesheet">
<style>
  :root {
    --teal: #336666;
    --heading: #2f6b69;
    --body-text: #555555;
    --rule: #cccccc;
    --white: #ffffff;
    --ring: #d2d2d2;
  }
  * { margin: 0; padding: 0; box-sizing: border-box; }
  html, body { width: 1200px; height: 900px; overflow: hidden; background: var(--white); }
  body { font-family: "Oxygen", "Segoe UI", sans-serif; position: relative; }

  .service { position: absolute; top: 36px; width: 270px; }
  .service-photo {
    width: 210px; height: 210px; border-radius: 50%;
    border: 4px solid var(--ring); margin-left: -4px;
  }
  .service-title {
    margin-top: 18px; font-size: 29.5px; font-weight: 400;
    color: var(--heading); white-space: nowrap; letter-spacing: 0.2px;
  }
  .service-list {
    list-style: none; margin-top: 12px; font-size: 18px; line-height: 29px;
    color: var(--body-text); width: 252px; hyphens: manual;
  }

  .rule { position: absolute; left: 0; width: 1200px; height: 10px; background: var(--rule); }
  .footer-band {
    position: absolute; left: 0; top: 489px; width: 1200px; height: 326px;
    background: var(--teal); color: var(--white);
  }
  .footer-col { position: absolute; top: 46px; }
  .footer-title { font-size: 20px; font-weight: 400; margin-bottom: 14px; }
  .footer-list { list-style: none; font-size: 17px; line-height: 29px; }
  .blog-list { width: 262px; margin-left: 2px; }
  .nav-list { line-height: 35px; margin-left: 8px; margin-top: 2px; }
  .contact-text { width: 270px; font-size: 17px; line-height: 23.5px; }
  .contact-text strong { font-weight: 700; }
  .contact-line { font-size: 17.5px; line-height: 29px; margin-left: 2px; }
  .contact-line.first { margin-top: 14px; }
  .contact-line b { font-weight: 700; margin-right: 12px; }
  .directions { font-size: 17.5px; margin-top: 12px; margin-left: 2px; }

  .copyright {
    position: absolute; top: 840px; left: 0; width: 1200px; text-align: center;
    font-size: 17px; color: var(--heading);
  }
</style>
</head>
<body>

  <section class="service" style="left:48px">
    <div class="service-photo" role="img" aria-label="Smiling senior couple with healthy teeth" style="background:radial-gradient(circle at 45% 45%, #f3d3b9, #d9a07c 60%, #c8936f)"></div>
    <h2 class="service-title">Beautiful Dentures</h2>
    <ul class="service-list">
      <li>What is a Denture?</li>
      <li>Who Needs a Denture?</li>
      <li>Just How Are Dentures Made?</li>
    </ul>
  </section>

  <section class="service" style="left:330px">
    <div class="service-photo" role="img" aria-label="Patient receiving a cosmetic dental check-up" style="background:radial-gradient(circle at 55% 40%, #f6e5dc, #e6eef6 55%, #9fc3ea)"></div>
    <h2 class="service-title">Cosmetic Dentistry</h2>
    <ul class="service-list">
      <li>Whiten Your Teeth</li>
      <li>Porcelain Veneers</li>
      <li>Clear Aligner Therapy Ortho&shy;dontics</li>
    </ul>
  </section>

  <section class="service" style="left:612px">
    <div class="service-photo" role="img" aria-label="Model of a dental implant between natural teeth" style="background:radial-gradient(circle at 50% 45%, #ffffff, #e4e4e4 60%, #bdbdbd)"></div>
    <h2 class="service-title">Dental Implant</h2>
    <ul class="service-list">
      <li>Anchorage to the jaw bone</li>
      <li>Replaces 1 or more missing teeth</li>
      <li>Stabilizes loose, floppy den&shy;tures</li>
    </ul>
  </section>

  <section class="service" style="left:894px">
    <div class="service-photo" role="img" aria-label="Dentist treating a relaxed patient in the chair" style="background:radial-gradient(circle at 50% 55%, #e9d2c2, #4fa49a 60%, #2f7f78)"></div>
    <h2 class="service-title">Sedation Dentistry</h2>
    <ul class="service-list">
      <li>Control Dental Fear with Se&shy;dation Dentistry</li>
      <li>Dental Pain Management</li>
      <li>Relaxed and Tranquil Treat&shy;ment</li>
    </ul>
  </section>

  <div class="rule" style="top:479px"></div>

  <footer class="footer-band">
    <div class="footer-col" style="left:40px">
      <h3 class="footer-title">Recent Blog Posts</h3>
      <ul class="footer-list blog-list">
        <li>Conscious Sedation: A Way to Deal with Anxiety at the Dentist's Office</li>
        <li>Pediatric Dentists and Their Im&shy;portance in Today's World</li>
        <li>Tooth Implant Facts</li>
        <li>Is Sedation Dentistry Cost Af&shy;fordable?</li>
      </ul>
    </div>

    <div class="footer-col" style="left:370px">
      <h3 class="footer-title">Services</h3>
      <ul class="footer-list">
        <li>Beautiful Dentures</li>
        <li>Cosmetic Dentistry</li>
        <li>Dental Implant</li>
        <li>Sedation Dentistry</li>
      </ul>
    </div>

    <div class="footer-col" style="left:616px">
      <h3 class="footer-title">Navigation</h3>
      <ul class="footer-list nav-list">
        <li>Home</li>
        <li>About Us</li>
        <li>Dental Services</li>
        <li>Blog</li>
        <li>Contact Us</li>
        <li>Testimonials</li>
      </ul>
    </div>

    <div class="footer-col" style="left:888px">
      <h3 class="footer-title">Contact Us</h3>
      <p class="contact-text">for all your general and cosmetic dental treatment and ask how to eliminate your dental pain and anxiety with <strong>sedation dentistry.</strong></p>
      <p class="contact-line first"><b>Email:</b>info@brelvoortdental.com</p>
      <p class="contact-line"><b>Phone:</b><strong>(555) 214-3068</strong></p>
      <p class="directions">Directions</p>
    </div>
  </footer>

  <div class="rule" style="top:815px"></div>

  <p class="copyright">©2014 Brelvoort Dental Care,</p>

</body>
</html>
```